We need a Photoshop specialist to design our outdoor billboard sign.

We need someone to design a billboard for us that will measure 8 feet wide 4 feet tall the Billboard needs to represent our company which is Brazos fine fitters and advertised that we do home theater installation home security and surveillance home automation and TV installation. Visit our website for more info BrazosFineFitters.example

Target Market(s)

homeowners in the area

Industry/Entity Type

It Company

Font styles to use
Sans Serif

Requirements
Must have
• company logo, pictures that represent our services, a list of our services, phone number, website address.

```html
<!DOCTYPE html>
<html lang="en">
<head>
<meta charset="utf-8">
<title>Brazos Fine Fitters — Billboard</title>
<link rel="stylesheet" href="https://fonts.googleapis.com/css2?family=Open+Sans:wght@400;600&family=Source+Sans+3:wght@300;400&display=swap">
<style>
  :root {
    --panel-dark: #141617;
    --panel-mid: #2b3133;
    --panel-teal: #1f4a4c;
    --smoke-orange: #f07a2a;
    --smoke-red: #c7301a;
    --smoke-pale: #fbe6d6;
    --paper: #f7f3f0;
    --heading-cream: #fff3e6;
    --band-red: #6e1a16;
    --band-red-dark: #3e0c0a;
    --title-brown: #94561f;
    --item-red: #c3262d;
    --frame-brown: #8a5428;
    --footer-dark: #3a1f0e;
    --footer-mid: #6d3c18;
    --footer-text: #ffffff;
  }
  * { box-sizing: border-box; margin: 0; padding: 0; }
  html, body { width: 1200px; height: 600px; overflow: hidden; background: var(--paper); }
  .billboard {
    position: relative; width: 1200px; height: 600px; overflow: hidden;
    background: var(--paper);
    font-family: "Open Sans", Arial, sans-serif;
  }
  .smoke-backdrop {
    position: absolute; left: 200px; top: 0; width: 1000px; height: 330px;
    background:
      radial-gradient(ellipse 260px 170px at 250px 60px, rgba(240,122,42,.85), transparent 70%),
      radial-gradient(ellipse 300px 180px at 830px 150px, rgba(199,48,26,.85), transparent 70%),
      radial-gradient(ellipse 340px 160px at 600px 90px, rgba(240,122,42,.7), transparent 72%),
      linear-gradient(180deg, var(--smoke-pale), var(--paper));
  }
  .side-panel {
    position: absolute; left: 0; top: 0; width: 200px; height: 600px;
    background:
      radial-gradient(ellipse 120px 140px at 40px 280px, var(--panel-teal), transparent 75%),
      linear-gradient(160deg, var(--panel-mid), var(--panel-dark) 60%);
    border-right: 4px solid #0b0c0c;
  }
  .side-brand {
    position: absolute; left: 0; top: 258px; width: 196px; text-align: center;
    font-weight: 600; font-size: 14px;
    letter-spacing: 1px; color: var(--heading-cream); text-transform: uppercase;
  }
  .side-brand .mark { display: inline-block; width: 9px; height: 9px; background: var(--heading-cream); margin-right: 6px; }

  .headline {
    position: absolute; right: 18px; top: -22px;
    font-family: "Source Sans 3", Arial, sans-serif; font-weight: 400;
    font-size: 168px; line-height: 1; color: var(--heading-cream);
    letter-spacing: 2px;
  }
  .headline-band {
    position: absolute; left: 562px; top: 123px; width: 630px; height: 38px;
    background: linear-gradient(180deg, var(--band-red), var(--band-red-dark));
    color: var(--heading-cream);
    font-family: "Source Sans 3", Arial, sans-serif; font-weight: 300;
    font-size: 31px; line-height: 38px; letter-spacing: 17px;
    text-align: right; padding-right: 6px; text-transform: uppercase;
  }

  .service-photo {
    position: absolute; width: 193px; height: 111px;
    border: 3px solid var(--frame-brown);
  }
  .photo-tv { left: 214px; top: 177px; background: linear-gradient(135deg, #e9e6e2, #9a9896); }
  .photo-sound { left: 214px; top: 297px; background: linear-gradient(180deg, #fafafa, #cfcfcf); }
  .photo-automation { left: 214px; top: 419px; background: linear-gradient(135deg, #dfe9ee, #7fa0b1); }
  .photo-theater { left: 733px; top: 297px; background: linear-gradient(180deg, #6a3a14, #1e1a18); }
  .photo-security { left: 733px; top: 419px; background: linear-gradient(135deg, #9db5c9, #6f8a4e); }

  .service { position: absolute; }
  .service-title {
    font-size: 20px; font-weight: 400; color: var(--title-brown); line-height: 24px;
    white-space: nowrap;
  }
  .service-list, .service-text {
    list-style: none; margin-left: 28px; margin-top: 4px;
    font-size: 16px; line-height: 23px; color: var(--item-red);
    white-space: nowrap;
  }
  .service-text { margin-left: 27px; }
  .svc-tv { left: 416px; top: 176px; }
  .svc-sound { left: 416px; top: 296px; }
  .svc-automation { left: 416px; top: 418px; }
  .svc-theater { left: 934px; top: 296px; }
  .svc-security { left: 936px; top: 420px; }

  .footer-brand {
    position: absolute; left: 208px; top: 566px; width: 172px; height: 34px;
    font-weight: 600; font-size: 14px; line-height: 34px; color: var(--footer-mid);
    text-transform: uppercase; white-space: nowrap;
  }
  .footer-bar {
    position: absolute; left: 383px; top: 566px; width: 817px; height: 34px;
    background: linear-gradient(90deg, var(--footer-mid), var(--footer-dark) 30%, var(--footer-dark) 80%, var(--footer-mid));
    color: var(--footer-text); font-size: 22px; line-height: 34px;
  }
  .contact { position: absolute; top: 0; display: flex; align-items: center; gap: 10px; height: 34px; white-space: nowrap; }
  .contact svg { width: 28px; height: 28px; }
  .contact-phone { left: 20px; }
  .contact-web { left: 294px; letter-spacing: .5px; }
</style>
</head>
<body>
<main class="billboard">
  <div class="smoke-backdrop" role="img" aria-label="Flowing orange and red smoke backdrop"></div>

  <aside class="side-panel" role="img" aria-label="Dark glossy panel with loudspeaker cones">
    <p class="side-brand"><span class="mark"></span>Brazos fine fitters</p>
  </aside>

  <h1 class="headline">Brazos</h1>
  <p class="headline-band">Fine Fitters</p>

  <div class="service-photo photo-tv" role="img" aria-label="Living room with wall-mounted television"></div>
  <div class="service-photo photo-sound" role="img" aria-label="Surround sound speaker set"></div>
  <div class="service-photo photo-automation" role="img" aria-label="Modern kitchen with a smartphone automation app"></div>
  <div class="service-photo photo-theater" role="img" aria-label="Home theater room with projector and audio gear"></div>
  <div class="service-photo photo-security" role="img" aria-label="Hand holding a phone security app in front of a house"></div>

  <section class="service svc-tv">
    <h2 class="service-title">TV Installation</h2>
    <ul class="service-list"><li>Table Top</li><li>On Wall</li><li>Fire Place</li></ul>
  </section>
  <section class="service svc-sound">
    <h2 class="service-title">Surround Sound Installation</h2>
    <ul class="service-list"><li>Basic Home Theater</li><li>5.1 Surround</li><li>7.1 Surround</li></ul>
  </section>
  <section class="service svc-automation">
    <h2 class="service-title">Surveillance Home Automation</h2>
    <p class="service-text">Mobile automation turns your<br>home into a play button. Wireless<br>control over your home elements</p>
  </section>
  <section class="service svc-theater">
    <h2 class="service-title">Home Theater Installation</h2>
    <p class="service-text">Complete turnkey home<br>theater packages Starting at<br>only $4999.</p>
  </section>
  <section class="service svc-security">
    <h2 class="service-title">Home Security</h2>
    <p class="service-text">Real time wireless security<br>applications give you security<br>monitoring and options</p>
  </section>

  <div class="footer-brand">Brazos fine fitters</div>
  <footer class="footer-bar">
    <div class="contact contact-phone">
      <svg viewBox="0 0 28 28" aria-hidden="true"><circle cx="14" cy="14" r="12.5" fill="none" stroke="#fff" stroke-width="2"/><path d="M10 8.5c1-.8 1.8-.6 2.3.3l1 1.8c.3.7.1 1.2-.5 1.6l-.8.5c.6 1.6 1.8 2.9 3.3 3.6l.6-.8c.4-.6 1-.7 1.6-.3l1.7 1.1c.8.5.9 1.4.1 2.3-1 1.1-2.4 1.3-4 .5-2.6-1.3-4.7-3.5-5.8-6.2-.6-1.6-.4-3.3.5-4.4z" fill="#fff"/></svg>
      <span>(555)014-2287</span>
    </div>
    <div class="contact contact-web">
      <svg viewBox="0 0 28 28" aria-hidden="true"><g fill="none" stroke="#fff" stroke-width="1.6"><circle cx="14" cy="14" r="12"/><ellipse cx="14" cy="14" rx="5.5" ry="12"/><path d="M2 14h24M4 8h20M4 20h20M14 2v24"/></g></svg>
      <span>www.BrazosFineFitters.example</span>
    </div>
  </footer>
</main>
</body>
</html>
```